Tolvex Engineers: Why you should hire us keepsake

New design. Open to plastic cards. We are an engineering firm that designs cell phone towers and commercial buildings. Please check out our website www.tolvexgrp.com for more details. We want people to remember our card and for it to be useful if possible. We want the same look and feel on these cards to be translated to other marketing material we may need such as brochures.

Target Market(s)

Architects, Developers and Telecommunication Carriers

Industry/Entity Type

Engineering

Contact Information for Business Card

Card with our company colors, logo, and innovative design with elements related to our industry.

Font styles to use
Sans Serif

Colors
9bcb3c
abd036
0255a3

Requirements
Must have
• Sleek and hip design
Nice to have
• Bright lime green and navy coloring that pops with an innovative design.
Should not have
• A basic and boring design

```html
<!DOCTYPE html>
<html lang="en">
<head>
<meta charset="utf-8">
<title>Tolvex Engineers – Business Card</title>
<link rel="stylesheet" href="https://fonts.googleapis.com/css2?family=Archivo+Black&family=Manrope:wght@400;500;600&display=swap">
<style>
  :root {
    --navy: #1b2f63;
    --navy-deep: #14244f;
    --lime: #3bd72f;
    --white: #ffffff;
    --ink: #1b2f63;
    --photo-a: #2c2e7a;
    --photo-b: #3d3f94;
    --backdrop: #e6e8ec;
  }
  * { box-sizing: border-box; margin: 0; padding: 0; }
  html, body { width: 1200px; height: 900px; overflow: hidden; }
  body {
    background: var(--backdrop);
    font-family: "Manrope", sans-serif;
    position: relative;
  }
  .card {
    position: absolute;
    left: 270px;
    width: 660px;
    height: 377px;
    border-radius: 22px;
    overflow: hidden;
    box-shadow: 0 10px 30px rgba(20, 36, 79, 0.18);
  }
  .card-front { top: 52px; background: var(--navy); }
  .card-back { top: 470px; background: var(--white); }

  .wordmark {
    position: absolute;
    left: 0; right: 0;
    top: 118px;
    text-align: center;
    font-family: "Archivo Black", sans-serif;
    font-size: 104px;
    line-height: 1;
    color: var(--lime);
    letter-spacing: -2px;
  }
  .offices {
    position: absolute;
    left: 40px;
    bottom: 34px;
    font-size: 15px;
    font-weight: 600;
    letter-spacing: 1.5px;
    color: var(--white);
    white-space: nowrap;
  }
  .offices .sep { color: var(--lime); margin: 0 6px; }

  .back-art { position: absolute; inset: 0; }

  .identity {
    position: absolute;
    left: 46px;
    top: 150px;
    padding-left: 16px;
    border-left: 6px solid var(--lime);
    box-shadow: -12px 0 0 var(--navy);
  }
  .person-name {
    font-size: 30px;
    font-weight: 600;
    color: var(--ink);
    letter-spacing: -0.5px;
    line-height: 1.1;
  }
  .person-title {
    font-size: 19px;
    color: var(--lime);
    line-height: 1.2;
  }
  .contacts {
    position: absolute;
    left: 72px;
    top: 238px;
    list-style: none;
    font-size: 19px;
    color: var(--ink);
    line-height: 27px;
  }
  .contacts li { display: flex; align-items: center; gap: 10px; }
  .contacts svg { width: 13px; height: 13px; flex: none; }
</style>
</head>
<body>

<section class="card card-front">
  <div class="wordmark">TOLVEX</div>
  <p class="offices">RIVERTON<span class="sep">|</span>OAKHAVEN<span class="sep">|</span>MILLBROOK<span class="sep">|</span>WEST FALLOW</p>
</section>

<section class="card card-back">
  <svg class="back-art" viewBox="0 0 660 377" width="660" height="377">
    <defs>
      <linearGradient id="photoTone" x1="0" y1="0" x2="1" y2="1">
        <stop offset="0" stop-color="var(--photo-a)"/>
        <stop offset="1" stop-color="var(--photo-b)"/>
      </linearGradient>
    </defs>
    <polygon role="img" aria-label="Photo of an engineer standing before a wall of sketched charts and plans"
             points="372,0 660,0 660,377 612,377 590,182 372,88" fill="url(#photoTone)"/>
    <polygon points="300,0 372,0 372,88 338,88" fill="var(--lime)"/>
    <polygon points="338,88 372,88 590,182 612,377 548,377 528,196 338,118" fill="var(--navy)"/>
    <polygon points="558,190 590,182 612,377 580,377" fill="var(--lime)"/>
  </svg>

  <div class="identity">
    <h1 class="person-name">Dana Reyes Colton</h1>
    <p class="person-title">Director</p>
  </div>

  <ul class="contacts">
    <li>
      <svg viewBox="0 0 16 16"><path d="M3 1l3 3-2 2c1 2 3 4 5 5l2-2 3 3-2 3C6 14 2 10 1 3z" fill="var(--lime)"/></svg>
      555.210.4410
    </li>
    <li>
      <svg viewBox="0 0 16 16"><rect x="4" y="1" width="8" height="14" rx="1.5" fill="none" stroke="var(--lime)" stroke-width="2"/></svg>
      555.310.7720
    </li>
    <li>
      <svg viewBox="0 0 16 16"><rect x="1" y="3" width="14" height="10" fill="none" stroke="var(--lime)" stroke-width="2"/><path d="M1 3l7 6 7-6" fill="none" stroke="var(--lime)" stroke-width="2"/></svg>
      dcolton@tolvexgrp.com
    </li>
    <li>
      <svg viewBox="0 0 16 16"><circle cx="8" cy="8" r="7" fill="var(--lime)"/><path d="M1 8h14M8 1v14" stroke="var(--white)" stroke-width="1.2"/></svg>
      www.tolvexgrp.com
    </li>
  </ul>
</section>

</body>
</html>
```